Visitenkarten- und Briefpapier Design - Logo vorhanden!
Zielgruppe
Wir sind eine Projektentwicklungs GmbH die Grundstücke kauft, projektiert und wieder verkauft. Eine zukünftige GmbH ist für den Innenausbau von neuen Häusern (EFH,DHH,MFH) gedacht. Wir sind ebenfalls für den Vertrieb von Häusern tätig.
Unsere Zielgruppe sind Endkunden im Immobilienbereich die Grundstücke und/oder Häuser bis Schlüsselfertig kaufen möchten, sowie Grundstückseigentümer die verkaufen wollen.
Wir benötigen Visitenkarten UND Briefpapier.
Aufgabenstellung
Bitte vorhandenes Logo verwenden.
Briefpapier:
Es soll ein ansprechendes modernes Design sein. Wir lassen uns gerne überraschen und versuchen schnellstmöglich Feedback zu geben.
Visitenkarte:
Es soll ein ansprechendes modernes Design sein. Die Visitenkarte bitte mit 2 Seiten, auf der Rückseite könnten wir uns das Dunkle BELTRO Logo sehr gut vorstellen (nur Logo).

```html
<!DOCTYPE html>
<html lang="de">
<head>
<meta charset="utf-8">
<title>BELTRO – Visitenkarte und Briefpapier</title>
<link rel="stylesheet" href="https://fonts.googleapis.com/css2?family=Source+Sans+3:wght@400;600;700&display=swap">
<style>
  :root {
    --stage: #505050;
    --paper: #ffffff;
    --navy: #143a55;
    --navy-deep: #0f1a3a;
    --navy-mid: #1d2d5c;
    --grey-text: #6b6b6b;
    --ink: #161616;
    --footer-text: #555555;
    --rule: #dcdcdc;
    --texture: #ececec;
  }
  * { margin: 0; padding: 0; box-sizing: border-box; }
  html, body { width: 1200px; height: 900px; overflow: hidden; }
  body {
    background: var(--stage);
    font-family: "Source Sans 3", "Myriad Pro", sans-serif;
    position: relative;
  }
  .sheet { position: absolute; overflow: hidden; }

  /* business card front */
  .card-front {
    left: 29px; top: 79px; width: 552px; height: 370px;
    background:
      radial-gradient(ellipse at 0% 100%, var(--texture) 0%, rgba(255,255,255,0) 55%),
      radial-gradient(ellipse at 100% 0%, var(--texture) 0%, rgba(255,255,255,0) 45%),
      var(--paper);
  }
  .brand {
    position: absolute;
    display: flex; align-items: center; gap: 8px;
    color: var(--navy);
    font-weight: 600;
    letter-spacing: 0.06em;
    line-height: 1;
  }
  .brand-dot { display: block; background: currentColor; }
  .card-front .brand { left: 62px; top: 170px; font-size: 32px; }
  .card-front .brand-dot { width: 12px; height: 12px; }
  .person-name {
    position: absolute; left: 272px; top: 66px;
    font-size: 27px; font-weight: 700; color: var(--navy);
  }
  .person-role {
    position: absolute; left: 272px; top: 98px;
    font-size: 14.5px; font-weight: 600; color: var(--grey-text);
  }
  .card-contact { position: absolute; left: 270px; top: 140px; color: var(--navy); }
  .card-contact .row {
    display: flex; align-items: flex-start; gap: 8px;
    font-size: 19px; font-weight: 600; line-height: 22.5px;
    margin-bottom: 25px;
  }
  .card-contact .row svg { flex: none; width: 18px; height: 22px; margin-top: 2px; fill: var(--navy); }

  /* business card back */
  .card-back {
    left: 29px; top: 465px; width: 551px; height: 370px;
    background: radial-gradient(ellipse at 50% 45%, var(--navy-mid) 0%, var(--navy-deep) 75%);
  }
  .card-back .brand {
    left: 0; right: 0; top: 148px; justify-content: center;
    color: var(--paper); font-size: 54px; font-weight: 400; gap: 14px;
  }
  .card-back .brand-dot { width: 16px; height: 16px; }

  /* letterhead */
  .letter {
    left: 599px; top: 49px; width: 575px; height: 814px;
    background:
      radial-gradient(ellipse at 0% 0%, var(--texture) 0%, rgba(255,255,255,0) 40%),
      radial-gradient(ellipse at 0% 100%, var(--texture) 0%, rgba(255,255,255,0) 35%),
      var(--paper);
  }
  .letter .brand { right: 54px; top: 96px; font-size: 28px; font-weight: 400; gap: 8px; }
  .letter .brand-dot { width: 10px; height: 10px; }
  .sender-line { position: absolute; left: 76px; top: 127px; font-size: 7.8px; color: var(--ink); }
  .recipient {
    position: absolute; left: 76px; top: 141px;
    font-size: 11.5px; line-height: 14px; color: var(--ink);
  }
  .letter-contact { position: absolute; left: 406px; top: 133px; color: var(--navy); }
  .letter-contact .row {
    display: flex; gap: 5px; font-size: 8px; font-weight: 600; line-height: 10.5px;
    margin-bottom: 10px;
  }
  .letter-contact .row svg { flex: none; width: 8px; height: 10px; fill: var(--navy); margin-top: 1px; }
  .letter-body {
    position: absolute; left: 76px; top: 305px; width: 460px;
    font-size: 11.5px; line-height: 14px; color: var(--ink);
  }
  .letter-body p { margin-bottom: 14px; white-space: nowrap; }
  .closing { position: absolute; left: 77px; top: 564px; font-size: 11.5px; color: var(--ink); }
  .signature-area {
    position: absolute; left: 86px; top: 587px; width: 72px; height: 56px;
    background: #f3f3f3; border-radius: 4px;
  }
  .footer-rule {
    position: absolute; left: 47px; right: 0; top: 724px;
    height: 1px; background: var(--rule);
  }
  .footer {
    position: absolute; top: 742px; left: 0; width: 100%;
    font-size: 9px; line-height: 11.6px; color: var(--footer-text);
  }
  .footer .col { position: absolute; top: 0; }
</style>
</head>
<body>

  <section class="sheet card-front">
    <div class="brand"><span class="brand-dot"></span>BELTRO</div>
    <h1 class="person-name">Max Mustermann</h1>
    <p class="person-role">Geschäftsführer</p>
    <div class="card-contact">
      <div class="row">
        <svg viewBox="0 0 24 30"><path d="M12 0C5.4 0 0 5.2 0 11.6 0 20 12 30 12 30s12-10 12-18.4C24 5.2 18.6 0 12 0zm0 16a4.6 4.6 0 1 1 0-9.2 4.6 4.6 0 0 1 0 9.2z"/></svg>
        <span>Musterstrasse 1<br>12345 Musterstadt</span>
      </div>
      <div class="row">
        <svg viewBox="0 0 24 24"><path d="M6.6 10.8a15 15 0 0 0 6.6 6.6l2.2-2.2c.3-.3.7-.4 1-.2 1.1.4 2.3.6 3.6.6.6 0 1 .4 1 1V20c0 .6-.4 1-1 1A17 17 0 0 1 3 4c0-.6.4-1 1-1h3.5c.6 0 1 .4 1 1 0 1.3.2 2.5.6 3.6.1.3 0 .7-.2 1z"/></svg>
        <span>0123 456 789</span>
      </div>
      <div class="row">
        <svg viewBox="0 0 24 24"><path d="M12 2a10 10 0 1 0 5 18.7l-.9-1.6A8.2 8.2 0 1 1 20.2 12v1.2c0 1.2-.8 2-1.8 2s-1.8-.8-1.8-2V7.5h-1.8v1a4.8 4.8 0 1 0 .4 6.6 3.5 3.5 0 0 0 3.2 2c2 0 3.6-1.6 3.6-3.9V12A10 10 0 0 0 12 2zm0 13a3 3 0 1 1 0-6 3 3 0 0 1 0 6z"/></svg>
        <span>email@beltro.de<br>www.beltro.de</span>
      </div>
    </div>
  </section>

  <section class="sheet card-back">
    <div class="brand"><span class="brand-dot"></span>BELTRO</div>
  </section>

  <section class="sheet letter">
    <div class="brand"><span class="brand-dot"></span>BELTRO</div>
    <p class="sender-line">Beltro, Musterstr. 1, 12345 Musterstadt</p>
    <p class="recipient">Mustermann Max<br>Musterstrasse 3<br>12345 Musterstadt</p>

    <div class="letter-contact">
      <div class="row">
        <svg viewBox="0 0 24 30"><path d="M12 0C5.4 0 0 5.2 0 11.6 0 20 12 30 12 30s12-10 12-18.4C24 5.2 18.6 0 12 0zm0 16a4.6 4.6 0 1 1 0-9.2 4.6 4.6 0 0 1 0 9.2z"/></svg>
        <span>Musterstrasse 1<br>12345 Musterstadt</span>
      </div>
      <div class="row">
        <svg viewBox="0 0 24 24"><path d="M6.6 10.8a15 15 0 0 0 6.6 6.6l2.2-2.2c.3-.3.7-.4 1-.2 1.1.4 2.3.6 3.6.6.6 0 1 .4 1 1V20c0 .6-.4 1-1 1A17 17 0 0 1 3 4c0-.6.4-1 1-1h3.5c.6 0 1 .4 1 1 0 1.3.2 2.5.6 3.6.1.3 0 .7-.2 1z"/></svg>
        <span>0123 456 789</span>
      </div>
      <div class="row">
        <svg viewBox="0 0 24 24"><path d="M12 2a10 10 0 1 0 5 18.7l-.9-1.6A8.2 8.2 0 1 1 20.2 12v1.2c0 1.2-.8 2-1.8 2s-1.8-.8-1.8-2V7.5h-1.8v1a4.8 4.8 0 1 0 .4 6.6 3.5 3.5 0 0 0 3.2 2c2 0 3.6-1.6 3.6-3.9V12A10 10 0 0 0 12 2zm0 13a3 3 0 1 1 0-6 3 3 0 0 1 0 6z"/></svg>
        <span>email@beltro.de<br>www.beltro.de</span>
      </div>
    </div>

    <div class="letter-body">
      <p>Sehr geehrte Herr Mustermann,</p>
      <p>Lorem ipsum dolor sit amet, consetetur sadipscing elitr, sed diam nonumy eir<br>mod tempor invidunt ut labore et dolore magna aliquyam erat, sed diam voluptua. A<br>t vero eos et accusam et justo duo dolores et ea rebum. Stet clita kasd gubergren, n<br>o sea takimata sanctus est Lorem ipsum dolor sit amet. Lorem ipsum dolor sit amet,<br>consetetur sadipscing elitr, sed diam nonumy eirmod tempor invidunt ut labore et d</p>
      <p>olore magna aliquyam erat, sed diam voluptua. At vero eos et accusam et justo duo dolo<br>res et ea rebum. Stet clita kasd gubergren, no sea takimata sanctus est Lorem ipsum</p>
      <p>&nbsp;dolor sit amet. Lorem ipsum dolor sit amet, consetetur sadipscing elitr,<br>diam nonumy eirmod tempor invidunt ut labore et dolore magna aliquya<br>m erat, sed diam voluptua. At vero eos et accusam et justo duo dolores e<br>t ea rebum. Stet clita kasd gubergren, no sea takimata sanctus est Lore<br>&nbsp;ipsum dolor sit amet.</p>
    </div>

    <p class="closing">mit freundlichen Grüßen,</p>
    <div class="signature-area" role="img" aria-label="Handschriftliche Unterschrift"></div>

    <div class="footer-rule"></div>

    <div class="footer">
      <div class="col" style="left:47px">Beltro Firma<br>Musterstr. 3<br>12345 Musterstadt</div>
      <div class="col" style="left:188px">Tel. 0123456789<br>Tel. 0123456789<br>Fax: 0123456789</div>
      <div class="col" style="left:325px">Öffnungszeiten<br>Mo-Fr.: 09:00 -18:00<br>Sa: 09:00 - 15:00</div>
      <div class="col" style="left:459px">www.beltro.de<br>email@beltro.de</div>
    </div>
  </section>

</body>
</html>
```